Ashcombe Vista Business Cards

We need business card designs for a modern home development, Ashcombe Vista. We would like to see modern looking designs- clean and simple but striking. I've attached some images of one of the homes so you can see the style of the homes we are putting on the market and perhaps they will inspire your design! I've also attached the logo- both horizontal and vertical. We need to use the logo on the card. I've also attached a sign that has a map of the development. If you can use that and still keep the card nice and clean, great. If not, it's not a problem to leave the map out completely.

```html
<!DOCTYPE html>
<html lang="en">
<head>
<meta charset="utf-8">
<title>Ashcombe Vista Business Cards</title>
<link rel="stylesheet" href="https://fonts.googleapis.com/css2?family=Open+Sans:wght@400;600;800&display=swap">
<style>
  :root {
    --backdrop: #e6e3de;
    --ink: #1b2327;
    --ink-soft: #252e33;
    --teal: #1f8a9c;
    --paper: #ffffff;
    --map-tone: #2b3439;
    --map-line: #8a9499;
  }
  * { box-sizing: border-box; margin: 0; padding: 0; }
  html, body { width: 1200px; height: 784px; overflow: hidden; }
  body {
    background: var(--backdrop);
    font-family: "Open Sans", Arial, sans-serif;
    display: flex;
    align-items: center;
    justify-content: center;
    gap: 40px;
  }
  .card {
    position: relative;
    width: 540px;
    height: 309px;
    border-radius: 4px;
    overflow: hidden;
    box-shadow: 0 6px 18px rgba(0,0,0,0.18);
  }

  /* Back side */
  .card-back { background: var(--ink); }
  .card-back .brand {
    position: absolute;
    top: 18px; left: 0; right: 0;
    display: flex; align-items: center; justify-content: center; gap: 8px;
  }
  .card-back .brand-mark { width: 18px; height: 18px; background: var(--paper); }
  .card-back .brand-name {
    color: var(--paper); font-weight: 800; font-size: 17px; letter-spacing: 0.5px;
    text-transform: uppercase;
  }
  .site-map {
    position: absolute;
    left: 44px; top: 58px; width: 452px; height: 214px;
    background: linear-gradient(160deg, var(--map-tone), var(--ink-soft));
    border: 1px solid var(--map-line);
  }

  /* Front side */
  .card-front { background: var(--ink); }
  .front-top {
    position: absolute; left: 0; top: 0; width: 100%; height: 148px;
    background: var(--paper);
  }
  .front-top .rule {
    position: absolute; left: 246px; right: 0; top: 100px; height: 4px;
    background: var(--teal);
  }
  .front-top .brand {
    position: absolute; left: 70px; top: 42px;
    display: flex; align-items: center; gap: 12px;
  }
  .front-top .brand-mark { width: 52px; height: 52px; background: var(--teal); }
  .front-top .brand-name {
    color: var(--ink); font-weight: 800; font-size: 34px; letter-spacing: 0.5px;
    text-transform: uppercase; line-height: 1;
  }
  .name-band {
    position: absolute; left: 0; top: 148px; width: 240px; height: 6px;
    background: var(--teal);
  }
  .holder { position: absolute; left: 28px; top: 164px; }
  .holder-name { color: var(--teal); font-size: 17px; font-weight: 600; line-height: 1.2; }
  .holder-role { color: var(--paper); font-size: 10px; font-weight: 600; margin-top: 1px; }
  .contacts {
    position: absolute; left: 28px; top: 226px; list-style: none;
  }
  .contacts li {
    display: flex; align-items: center; gap: 7px;
    color: var(--paper); font-size: 11px; line-height: 16px;
  }
  .contacts svg { width: 11px; height: 11px; fill: var(--teal); flex: none; }
</style>
</head>
<body>

  <section class="card card-back" aria-label="Card back">
    <div class="brand">
      <span class="brand-mark"></span>
      <span class="brand-name">Ashcombe Vista</span>
    </div>
    <div class="site-map" role="img" aria-label="Street map of the Ashcombe Vista development with home lots marked"></div>
  </section>

  <section class="card card-front" aria-label="Card front">
    <div class="front-top">
      <div class="brand">
        <span class="brand-mark"></span>
        <span class="brand-name">Ashcombe Vista</span>
      </div>
      <div class="rule"></div>
    </div>
    <div class="name-band"></div>
    <div class="holder">
      <p class="holder-name">Daniel R. Fenwick</p>
      <p class="holder-role">Developer, Investor</p>
    </div>
    <ul class="contacts">
      <li>
        <svg viewBox="0 0 24 24" aria-hidden="true"><path d="M6.6 10.8a15 15 0 0 0 6.6 6.6l2.2-2.2c.3-.3.7-.4 1-.2 1.1.4 2.3.6 3.6.6.6 0 1 .4 1 1V20c0 .6-.4 1-1 1A17 17 0 0 1 3 4c0-.6.4-1 1-1h3.5c.6 0 1 .4 1 1 0 1.3.2 2.5.6 3.6.1.3 0 .7-.2 1z"/></svg>
        555.204.3180
      </li>
      <li>
        <svg viewBox="0 0 24 24" aria-hidden="true"><path d="M7 1h10a2 2 0 0 1 2 2v18a2 2 0 0 1-2 2H7a2 2 0 0 1-2-2V3a2 2 0 0 1 2-2zm0 3v14h10V4zm5 15.5a1 1 0 1 0 0 2 1 1 0 0 0 0-2z"/></svg>
        555.318.0462
      </li>
      <li>
        <svg viewBox="0 0 24 24" aria-hidden="true"><path d="M2 5h20v14H2zm2 2v.5l8 5 8-5V7zm0 2.8V17h16V9.8l-8 5z"/></svg>
        dfenwick@mailpost.net
      </li>
      <li>
        <svg viewBox="0 0 24 24" aria-hidden="true"><path d="M12 3l10 9h-3v9h-5v-6h-4v6H5v-9H2z"/></svg>
        2740 Larkfield Avenue, Brookhaven, TX 75990
      </li>
    </ul>
  </section>

</body>
</html>
```